WordPress Website for Pain Relief Clinic

I need a WordPress website designed for my laser pain relief clinic. It needs to be a professional, responsive design with 7 pages: Home, Why Choose Us, Treatable Conditions, Testimonials, FAQ, Franchising, Contact Us. Here is logo: https://files.brivoltcdn.com/media.t-w-e-n.com/sitebuilder/472/CalvexaLogoHighQuality.png

Target Market(s)

people with pain,elderly adults,injuries,soreness

Industry/Entity Type

Clinic

Number of Pages Required

5+ page

Colors
0792cd
85abd2

```html
<!DOCTYPE html>
<html lang="en">
<head>
<meta charset="utf-8">
<title>Calvexa Pain Treatment Center</title>
<link href="https://fonts.googleapis.com/css2?family=Lato:wght@300;400;700&display=swap" rel="stylesheet">
<style>
:root{
  --page:#ffffff;
  --dark:#1c1c1c;
  --nav:#1a1a1a;
  --rule:#a9a9a9;
  --text:#f2f2f2;
  --muted:#d9d9d9;
  --accent-red:#e02424;
  --search-red:#c81e1e;
  --highlight:#f06060;
  --brand-blue:#1f6fc8;
  --cta-blue:#0f6bc4;
  --form-blue:#144a7c;
  --field:#e4e4e4;
  --submit:#9b8c8a;
}
*{margin:0;padding:0;box-sizing:border-box}
html,body{width:1200px;height:1000px;overflow:hidden;background:var(--page);font-family:'Lato',sans-serif}
.site{position:absolute;left:44px;top:0;width:1112px;height:1000px;background:var(--dark);overflow:hidden}
.site > *{position:absolute}
.brand{left:101px;top:20px;font-size:42px;font-weight:700;color:var(--brand-blue);letter-spacing:-1px;line-height:50px}
.search{left:618px;top:31px;width:265px;height:34px;background:#efefef;border:1px solid #ccc}
.search svg{position:absolute;left:8px;top:6px}
.search-btn{left:887px;top:31px;width:90px;height:34px;background:var(--search-red);color:#fff;font-size:14px;letter-spacing:1px;display:flex;align-items:center;justify-content:center}
.hero-photo{left:500px;top:95px;width:612px;height:430px;background:radial-gradient(ellipse at 45% 50%,#8a3a3a 0%,#6a6a6a 18%,#9a9a9a 38%,#4a4a4a 62%,var(--dark) 90%)}
.hero-fade{left:0;top:95px;width:760px;height:430px;background:linear-gradient(90deg,var(--dark) 55%,rgba(28,28,28,0));}
.hero-glow{left:0;top:141px;width:600px;height:380px;background:radial-gradient(ellipse at 30% 10%,rgba(110,110,110,.45),rgba(28,28,28,0) 70%)}
.nav-rule{left:0;top:89px;width:824px;height:6px;background:var(--rule)}
.nav{left:0;top:95px;width:824px;height:46px;background:var(--nav);display:flex;align-items:center;padding-left:101px;font-size:15px;color:var(--text)}
.nav a{color:inherit;text-decoration:none}
.nav a.current{color:var(--accent-red)}
.nav .sep{margin:0 12px}
.headline{left:98px;top:172px;font-weight:300;font-size:74px;line-height:78px;color:#fff;letter-spacing:1px}
.headline strong{font-weight:700}
.subline{left:98px;top:326px;width:404px;text-align:center;font-weight:700;font-size:19px;line-height:24px;color:#fff}
.subline em{font-style:normal;color:var(--highlight)}
.cta{left:103px;top:393px;width:392px;height:40px;border-radius:6px;background:var(--cta-blue);color:#fff;font-weight:700;font-size:15px;display:flex;align-items:center;justify-content:center}
.intro{left:99px;top:511px;width:910px;font-size:14px;line-height:17.5px;color:var(--text)}
.gallery-tile{width:171px;height:127px}
.t1{left:101px;top:653px;background:linear-gradient(135deg,#d9c6b5,#f1ece6 60%,#b48a6c)}
.t2{left:280px;top:653px;background:linear-gradient(135deg,#e8d8c8,#b88c6c 55%,#f2f0ee)}
.t3{left:101px;top:789px;background:linear-gradient(135deg,#7a5a3a,#d8a88a 50%,#eeeae6)}
.t4{left:280px;top:789px;background:linear-gradient(135deg,#f0eeea,#c89a80 50%,#8a6a52)}
.signup{left:469px;top:653px;width:290px;height:219px;background:var(--form-blue);border-radius:8px;padding:22px 25px 0}
.signup h2{font-size:18px;font-weight:400;color:#fff;text-align:center;margin-bottom:19px}
.field{height:22px;background:var(--field);margin-bottom:15px;font-size:9px;color:#555;display:flex;align-items:center;padding-left:8px;position:relative}
.field::after{content:"";position:absolute;right:10px;top:0;width:1px;height:22px;background:#bbb}
.submit{width:104px;height:21px;border-radius:11px;background:var(--submit);color:#fff;font-size:11px;font-weight:700;display:flex;align-items:center;justify-content:center;margin-top:-2px}
.signup-note{left:470px;top:885px;width:300px;font-size:14px;line-height:17px;color:var(--text)}
.divider{left:792px;top:655px;width:2px;height:266px;background:#e8e8e8}
.contact{left:821px;top:650px;color:var(--text);font-size:16px;line-height:20px}
.contact h3{font-weight:300;font-size:20px;margin-bottom:18px}
.contact .hours-title{font-weight:700;font-size:15px;margin-top:37px;margin-bottom:18px}
.contact strong{font-size:17px}
.footer{left:0;top:965px;width:1112px;height:35px;background:var(--accent-red);color:#fff;font-size:14px;display:flex;align-items:center;padding-left:99px}
.social{position:absolute;top:5px;width:24px;height:24px;border:2px solid #fff;border-radius:50%}
.s1{left:919px}.s2{left:953px}.s3{left:987px}
</style>
</head>
<body>
<div class="site">
  <div class="hero-photo" role="img" aria-label="Black and white photo of hands clasping a knee with red glow marking the pain"></div>
  <div class="hero-fade"></div>
  <div class="hero-glow"></div>

  <div class="brand">Calvexa</div>
  <div class="search">
    <svg width="24" height="24" viewBox="0 0 24 24"><circle cx="9" cy="9" r="6.5" fill="none" stroke="#888" stroke-width="2"/><line x1="14" y1="14" x2="21" y2="21" stroke="#888" stroke-width="3" stroke-linecap="round"/></svg>
  </div>
  <div class="search-btn">search</div>

  <div class="nav-rule"></div>
  <nav class="nav">
    <a class="current">Home</a><span class="sep">|</span>
    <a>Why Choose Us</a><span class="sep">|</span>
    <a>Treatable Conditions</a><span class="sep">|</span>
    <a>Testimonials</a><span class="sep">|</span>
    <a>FAQ</a><span class="sep">|</span>
    <a>Franchising</a><span class="sep">|</span>
    <a>Contact Us</a>
  </nav>

  <h1 class="headline">SUFFERING<br>FROM <strong>PAIN</strong>?</h1>
  <p class="subline">relive back pain, knee pain and shoulder pain using our <em>specialized laser treatment</em></p>
  <div class="cta">BOOK AN APPOINTMENT NOW</div>

  <p class="intro">Calvexa Pain Treatment Center Lorem ipsum dolor sit amet, consectetur adipiscing elit, sed do eiusmod tempor incididunt ut labore et dolore magna aliqua. Ut enim ad minim veniam, quis nostrud exercitation ullamco laboris nisi ut aliquip ex ea commodo consequat. Duis aute irure dolor in reprehenderit in voluptate velit esse cillum dolore eu fugiat nulla pariatur. Excepteur sint occaecat cupidatat non proident, sunt in culpa qui officia deserunt mollit anim id est laborum.</p>

  <div class="gallery-tile t1" role="img" aria-label="Patient receiving laser treatment on the neck"></div>
  <div class="gallery-tile t2" role="img" aria-label="Laser device applied to the lower back"></div>
  <div class="gallery-tile t3" role="img" aria-label="Laser treatment on an elbow"></div>
  <div class="gallery-tile t4" role="img" aria-label="Laser device glowing red on a knee"></div>

  <form class="signup">
    <h2>Sign up for a FREE consultation</h2>
    <div class="field">Name</div>
    <div class="field">Email Address</div>
    <div class="field">Country of Residence</div>
    <div class="submit">Submit</div>
  </form>
  <p class="signup-note">Sign up for our email newsletter and get a FREE consultation from our World Class Doctors!</p>

  <div class="divider"></div>
  <div class="contact">
    <h3>CALL US TODAY!</h3>
    <div>Tel: 555-014-2368</div>
    <div>E-mail: enquiry@calvexacare.com</div>
    <div class="hours-title">Operating Hours:</div>
    <div>Weekdays</div>
    <strong>8:00AM to 7:00PM</strong>
    <div>Weekend</div>
    <strong>8:00AM to 3:00PM</strong>
  </div>

  <footer class="footer">
    Calvexa Pain Treatment Center&nbsp;<strong>© 2015</strong>
    <span class="social s1"></span><span class="social s2"></span><span class="social s3"></span>
  </footer>
</div>
</body>
</html>
```